Online Psychiatry business - Business Card

I need a business card design. The target audience is busy professionals of any field (this therapy appeals best to 24-35 year olds). It involves psychiatry by tele-medicine (or video-conference). Nothing on it should be a giveaway that it's about mental health. Professional design with silver or gold as the primary colors appeals to me. The card must be as simple and as uncluttered as possible. Some color and flowing design on the edge of the card appeals to me.
CrestMindLink.com should probably appear in the center of the card and stand out, i.e. bold lettering, and easy to read, no cursive, but Ariel Black. Some where below this, should appear "No Spare Hour to Look After Yourself? Make one now." Since this isn't office based, I don't think an office address is necessary and limits clutter.
Information that does need to appear is my name: Gerald Whitcombe, MD
General phone number: 541-876-2209. I'm hoping to get an 24-hour answering service soon so leave a little room for this. In addition I want to include two email addresses:
CrestMindLink@maildrop-box.com and CrestMind247@maildrop-box.com
Updates

I like the designs. I would like someone to put the website in bold in the center

 as most have been doing with a smaller font reminder nearby saying "No time" etc.
but I'd like to put my name down in the corner with the rest of the contact material.
Black print against a white or grey background appeals to me, with darker silver artwork near the sides (simple abstract, like wavy lines or something you can one up with that works. 
thanks

I ve tried to provide as much feedback as possible given my time limits, so if you have extra questions, please feel free to email. I tried to attach a file of a business card I really like but make be difficult to actually manufacture. I'm going to send you a link to the photo. The card has a pull tab. There is not much information on the outside. In fact, if you were to design the outside, I would just print : No Spare Hour to Look After Yourself? Make one now.

When you pull the tab the remaining information is on the bottom half of the card. Please don't use the color pink!!!!
http://www.layoutgallerypost.com/2009/05/100-clever-card-ideas/
It is the 39th photo on the list, about 2/3ds of the way down the page. It is titled: Faltenkästli

#7 and #16 have an appeal to me, except for the dot patterns
Hope this helps

I'm running out of time and energy. I 've been trying to give do down the list and give  individual feedback but I won't be able to do that anymore.

So if you have any specific questions, write me, and again thank you for all your effort!!

I know i received your files, including your zip files, Plonix,

but Gideon, did you send me the files including ZIP on project 5914386?
thanks

Target Market(s)

Working professionals and executive, attorneys, etc.

Industry/Entity Type

Business

Logo Text

Don't Have Time to Take Care of Yourself? Think Again.

Logo styles of interest
Pictorial/Combination Logo
Wordmark Logo
Other font styles liked:
• Ariel Black appeals to me the most

Requirements
Must have
• Want to emphasize that the website must be obvious, easily found (The CrestMindLink.com)
For that reason i'd like the card to be white, and minimal decoration on one or both sides just to add some style and color
Nice to have
• A Very uncluttered, elegant design, and something that makes it stick in your head-doesn't everyone want the last?
Should not have
• Nothing on the card that give it away that this is about psychiatry, such as brain or other symbol, but also nothing that gives it away as a medical business, such as a stethoscope or red cross or anything.

```html
<!DOCTYPE html>
<html lang="en">
<head>
<meta charset="utf-8">
<title>CrestMindLink.com – Business Card</title>
<link rel="stylesheet" href="https://fonts.googleapis.com/css2?family=Archivo+Black&family=Arimo:wght@400;700&display=swap">
<style>
  :root {
    --card-grey: #dcdcdc;
    --edge-blue-deep: #7ea7cb;
    --edge-blue-mid: #86c3e6;
    --edge-blue-light: #c6e4f4;
    --ink: #000000;
    --ink-soft: #1e1e1e;
    --ink-muted: #2e2e2e;
  }
  html, body {
    margin: 0;
    padding: 0;
    width: 1200px;
    height: 686px;
    overflow: hidden;
    background: var(--card-grey);
  }
  .card {
    position: relative;
    width: 1200px;
    height: 686px;
    background: var(--card-grey);
    overflow: hidden;
    font-family: "Arimo", Arial, sans-serif;
    color: var(--ink);
  }
  .edge-art {
    position: absolute;
    inset: 0;
    width: 1200px;
    height: 686px;
  }
  .website {
    position: absolute;
    left: 260px;
    top: 288px;
    margin: 0;
    font-family: "Archivo Black", "Arial Black", sans-serif;
    font-size: 66px;
    font-weight: 400;
    letter-spacing: -1.6px;
    line-height: 1;
    white-space: nowrap;
  }
  .tagline {
    position: absolute;
    left: 265px;
    top: 370px;
    margin: 0;
    font-size: 27px;
    line-height: 1;
    white-space: nowrap;
    color: var(--ink-soft);
  }
  .tagline .tagline-close {
    font-size: 28px;
    position: relative;
    top: 4px;
  }
  .contact {
    position: absolute;
    left: 38px;
    top: 490px;
    margin: 0;
    font-style: normal;
  }
  .contact-name {
    margin: 0 0 14px;
    font-size: 34px;
    font-weight: 700;
    line-height: 1;
    white-space: nowrap;
  }
  .contact-line {
    margin: 0;
    font-size: 24px;
    line-height: 36px;
    color: var(--ink-muted);
    white-space: nowrap;
  }
  .contact-line.phone {
    color: var(--ink-soft);
  }
</style>
</head>
<body>
  <main class="card">
    <svg class="edge-art" viewBox="0 0 1200 686" aria-hidden="true">
      <defs>
        <radialGradient id="edgeGlow" cx="1120" cy="343" r="420" gradientUnits="userSpaceOnUse">
          <stop offset="0" stop-color="var(--edge-blue-light)"/>
          <stop offset="0.35" stop-color="var(--edge-blue-mid)"/>
          <stop offset="1" stop-color="var(--edge-blue-deep)"/>
        </radialGradient>
      </defs>
      <rect x="740" y="0" width="460" height="686" fill="url(#edgeGlow)"/>
      <polygon points="0,0 748,0 1185,343 748,686 0,686" fill="var(--card-grey)"/>
    </svg>

    <h1 class="website">CrestMindLink.com</h1>
    <p class="tagline">No Spare Hour to Look After Yourself? <span class="tagline-close">Make one now.</span></p>

    <address class="contact">
      <p class="contact-name">Gerald Whitcombe, MD</p>
      <p class="contact-line phone">541-876-2209</p>
      <p class="contact-line">CrestMindLink@maildrop-box.com</p>
      <p class="contact-line">CrestMind247@maildrop-box.com</p>
    </address>
  </main>
</body>
</html>
```